B2B telecom company need web design

We need a web design for our corporate web site. The company exists since almost 10 years.
This is a DESIGN contest, you're expected to provide design only, NOT the whole website. The winner will have to provide the HTML template (with Lorem Ipsum content) and the CSS files of his design.
Our initial product is SMS peering in P2P (you send a SMS to a friend in a foreign country, great chance that your operator route your SMS to us that we route to the recipient). We're launching a bulk SMS service (marketing and application to SMS).
Target is mostly corporate, usually big corporate (operators, contents providers...) where use of SMS is part of the main business.
The web site is composed of 1 landing page and 7 content pages (plan is given for your information, all content page are using the same template and the same design, you do NOT need to make one design per page) :
* About US
Company Profile
They trust us
The Volnor Team
Partners
Contact us
* Solution
P2P SMS
A2P SMS
You only need to submit the landing page and a template page for the content (with h1, h2, h3 and h4).
Design must be based on our new logo (see attached file).
Our current web site http://www.volnor-example.com
The winner of the contest will have to provide state of the art HTML template and CSS files of his design. Photo used shall be downloaded from Pixelbrook (provide the ID of the picture that we purchase file).
Target Market(s)
Telecom operator. SMS Peering hubs. Bulk SMS.
Industry/Entity Type
It Company
Number of Pages Required
2 page

```html
<!DOCTYPE html>
<html lang="en">
<head>
<meta charset="utf-8">
<title>Volnor Mobile — SMS Exchange</title>
<link href="https://fonts.googleapis.com/css2?family=Open+Sans:wght@300;400;600;700&display=swap" rel="stylesheet">
<style>
:root{
  --green:#7cbf2b;
  --green-dark:#5aa828;
  --green-light:#92d150;
  --band:#86c226;
  --ink:#2b2b2b;
  --text:#555;
  --muted:#999;
  --line:#d9d9d9;
  --grey-bg:#f4f4f4;
  --white:#fff;
}
*{box-sizing:border-box;margin:0;padding:0}
html,body{width:1200px;height:3322px;overflow:hidden}
body{font-family:"Open Sans",Arial,sans-serif;color:var(--text);background:var(--white);position:relative}
.section{position:absolute;left:0;width:1200px}
.abs{position:absolute}

/* hero */
.hero{top:0;height:673px;background:linear-gradient(120deg,var(--green-dark) 0%,#6ec236 45%,var(--green-light) 100%)}
.site-nav{left:133px;top:27px;width:934px;height:71px;background:var(--white);display:flex;align-items:center;padding:0 24px;justify-content:space-between}
.brand{font-size:20px;font-weight:600;color:var(--ink);letter-spacing:1px;display:flex;align-items:center;gap:8px}
.brand .mark{width:10px;height:10px;background:var(--green)}
.nav-links{display:flex;gap:42px;list-style:none;font-size:12px;color:var(--ink);text-transform:uppercase}
.nav-links .active{color:var(--green);font-weight:600}
.hero-title{left:160px;top:202px;font-size:33px;font-weight:300;color:var(--white)}
.hero-title strong{font-weight:700}
.hero-lead{left:160px;top:256px;width:360px;font-size:17px;font-weight:600;line-height:25px;color:var(--white)}
.hero-list{left:160px;top:344px;list-style:none;font-size:13px;color:var(--white)}
.hero-list li{height:27.5px;padding-left:20px;position:relative}
.hero-list li::before{content:"›";position:absolute;left:0;top:-3px;font-size:17px}
.btn-learn{left:160px;top:475px;width:158px;height:52px;border:2px solid var(--white);color:var(--white);font-weight:600;font-size:16px;display:flex;align-items:center;justify-content:center;gap:10px;text-transform:uppercase}
.hero-map{left:480px;top:190px;width:560px;height:340px;border-radius:8px;background:radial-gradient(ellipse at center,rgba(255,255,255,.35),rgba(255,255,255,.08) 70%,transparent)}
.slide-arrow{top:316px;width:44px;height:44px;border:2px solid rgba(255,255,255,.8);border-radius:50%;display:flex;align-items:center;justify-content:center}
.slide-dots{top:636px;left:0;width:1200px;display:flex;justify-content:center;gap:6px}
.slide-dots span{width:9px;height:9px;border-radius:50%;background:var(--white)}
.slide-dots span.on{background:transparent;border:2px solid var(--white)}

/* headings */
.section-title{left:0;width:1200px;display:flex;justify-content:center;align-items:center;gap:22px;font-size:21px;font-weight:700;color:var(--ink);text-transform:uppercase}
.section-title::before,.section-title::after{content:"";width:48px;height:1px;background:var(--line)}
.section-intro{left:230px;width:740px;text-align:center;font-size:14px;line-height:29px;color:var(--text)}

/* services */
.services{top:673px;height:489px}
.service{width:260px}
.service svg{position:absolute;left:-62px;top:-6px}
.service h3{font-size:13px;font-weight:700;color:var(--ink);margin-bottom:10px}
.service p{font-size:10.5px;line-height:19px;color:var(--text)}

/* demo */
.demo{top:1162px;height:525px;background:var(--band)}
.window{background:#a6d377;border-radius:3px;overflow:hidden}
.window .bar{height:18px;background:#4f8a1c;display:flex;gap:5px;align-items:center;padding-left:8px}
.window .bar i{width:6px;height:6px;border-radius:50%;background:#b9e07c}
.window.back{background:#8aab58;opacity:.9}
.window.front{background:#c3e39b}
.window .toolbar{height:20px;background:#a6d377;margin:0}
.demo-label{left:367px;width:469px;top:1406px;text-align:center;font-size:24px;letter-spacing:18px;color:#3f6b15;font-weight:300}
.demo-brand{left:367px;width:469px;top:1440px;text-align:center;font-size:28px;font-weight:600;color:#4b7f1b;letter-spacing:1px}
.play{left:570px;top:1392px;width:60px;height:60px;border-radius:50%;background:var(--white);display:flex;align-items:center;justify-content:center}

/* testimonial */
.testimonial{top:1687px;height:624px;background:var(--grey-bg)}
.quote-mark{left:0;width:1200px;top:1730px;text-align:center;font-size:110px;line-height:1;color:#bdbdbd;font-weight:700;font-family:Georgia,serif}
.avatar{left:562px;top:1851px;width:76px;height:76px;border-radius:50%;border:3px solid var(--white);background:linear-gradient(#d9d9d9,#b8b8b8);box-shadow:0 0 0 1px #ddd}
.person{left:0;width:1200px;top:1943px;text-align:center}
.person .name{font-size:12px;font-weight:700;color:var(--ink)}
.person .role{font-size:9px;color:var(--muted);text-transform:uppercase}
.quote-text{left:244px;width:712px;top:2017px;text-align:center;font-size:14px;line-height:28px;color:var(--text)}
.quote-dots{top:2193px;left:0;width:1200px;display:flex;justify-content:center;gap:6px}
.quote-dots span{width:9px;height:9px;border-radius:50%;background:var(--green)}
.quote-dots span.on{background:transparent;border:2px solid var(--green)}

/* contact */
.contact{top:2311px;height:689px;overflow:hidden}
.say-hello{left:160px;top:2672px;font-size:18px;color:var(--ink)}
.field{left:160px;width:427px;border-bottom:1px solid var(--line);font-size:10px;color:var(--muted);padding-bottom:10px}
.send{left:160px;top:2906px;display:flex;align-items:center;gap:20px;font-size:12px;color:var(--ink)}
.phone{left:650px;top:2570px;width:400px;height:430px;border-radius:40px 40px 0 0;background:linear-gradient(90deg,transparent 0 37%,#e2e2e2 37% 39%,var(--green) 39% 96%,#e2e2e2 96%)}

/* footer */
.footer{top:3000px;height:322px;border-top:4px solid var(--green);background:var(--white)}
.footer h4{font-size:11px;font-weight:700;color:var(--ink)}
.footer p,.footer li{font-size:9.5px;line-height:18px;color:var(--muted);list-style:none}
.footer .links li{line-height:24px;color:var(--text)}
.subscribe-box{left:387px;top:3173px;width:202px;height:29px;border:1px solid #ccc;display:flex;align-items:center;justify-content:flex-end;padding-right:12px}
.footer-brand{left:836px;top:3150px;font-size:19px}
.copyright{left:836px;top:3198px}
</style>
</head>
<body>

<header class="section hero">
  <nav class="abs site-nav">
    <div class="brand"><span class="mark"></span>VOLNOR mobile</div>
    <ul class="nav-links">
      <li class="active">Home</li><li>Services</li><li>About</li><li>News</li><li>Contact us</li>
    </ul>
  </nav>

  <h1 class="abs hero-title">Introducing <strong>VOLNOR</strong></h1>
  <p class="abs hero-lead">VOLNOR Mobile Exchange leads the world in the delivery, billing, and settlement of mobile messaging services.</p>
  <ul class="abs hero-list">
    <li>Global Reach</li><li>Superior Infrastructure</li><li>Comprehensive Reporting</li><li>Integrated Clearing + Settlement</li>
  </ul>
  <div class="abs btn-learn">
    <svg width="20" height="24" viewBox="0 0 20 24" fill="none" stroke="#fff" stroke-width="1.6"><path d="M10 2a7 7 0 0 0-4 12.8V18h8v-3.2A7 7 0 0 0 10 2z"/><path d="M7 21h6"/></svg>
    Learn how
  </div>

  <div class="abs hero-map" role="img" aria-label="World map illustration with message routing path between sent and received callouts"></div>

  <div class="abs slide-arrow" style="left:38px">
    <svg width="14" height="14" viewBox="0 0 14 14" fill="none" stroke="#fff" stroke-width="2"><path d="M9 2 4 7l5 5"/></svg>
  </div>
  <div class="abs slide-arrow" style="left:1118px">
    <svg width="14" height="14" viewBox="0 0 14 14" fill="none" stroke="#fff" stroke-width="2"><path d="M5 2l5 5-5 5"/></svg>
  </div>
  <div class="abs slide-dots"><span class="on"></span><span></span><span></span><span></span></div>
</header>

<section class="section services">
  <h2 class="abs section-title" style="top:78px">Our services</h2>
  <p class="abs section-intro" style="top:162px">VOLNOR's global connectivity and network reliability inspire confidence that messages get delivered successfully, and that related revenue is processed quickly. Customers include leading mobile operators worldwide.</p>

  <div class="abs service" style="left:236px;top:295px">
    <svg width="32" height="32" viewBox="0 0 32 32" fill="none" stroke="#999" stroke-width="1.3"><path d="M5 27 27 5M5 5l22 22M4 9l5-5M23 28l5-5"/></svg>
    <h3>365 Interoperability Services</h3>
    <p>Connect your customers, 365 days a year. Global operators—VOLNOR &amp; Partners are the leader in messaging interoperability, using both IP and SS7.</p>
  </div>
  <div class="abs service" style="left:536px;top:295px">
    <svg width="32" height="32" viewBox="0 0 32 32" fill="none" stroke="#999" stroke-width="1.3"><circle cx="7" cy="22" r="3"/><circle cx="16" cy="12" r="3"/><circle cx="26" cy="18" r="3"/><path d="M9 20l5-6M19 13l5 4"/></svg>
    <h3>Reporting + Statistics</h3>
    <p>Using our comprehensive Web-based reporting tools, customers track and analyze traffic trends such as message origination and termination by operator, etc.</p>
  </div>
  <div class="abs service" style="left:836px;top:295px">
    <svg width="32" height="32" viewBox="0 0 32 32" fill="none" stroke="#999" stroke-width="1.3"><path d="M3 15 29 4 22 28l-7-9zM15 19l14-15"/></svg>
    <h3>Integrated Clearing + Settlement</h3>
    <p>We ensure your revenue gets rapidly delivered in currencies worldwide, VOLNOR Mobile Exchange enables companies to distribute messages and content.</p>
  </div>
</section>

<section class="section demo">
  <div class="abs window back" style="left:233px;top:174px;width:736px;height:237px"><div class="bar"><i></i><i></i><i></i></div></div>
  <div class="abs window front" style="left:367px;top:107px;width:469px;height:318px">
    <div class="bar"><i></i><i></i><i></i></div>
    <div class="toolbar"></div>
  </div>
</section>
<div class="abs demo-label">SHOW&nbsp;&nbsp;&nbsp;&nbsp;&nbsp;&nbsp;DEMO</div>
<div class="abs demo-brand">VOLNOR mobile</div>
<div class="abs play">
  <svg width="22" height="24" viewBox="0 0 22 24" fill="none" stroke="#6aa52a" stroke-width="2"><path d="M4 2l16 10L4 22z"/></svg>
</div>

<section class="section testimonial"></section>
<div class="abs quote-mark">“</div>
<div class="abs avatar" role="img" aria-label="Portrait photo of the quoted executive"></div>
<div class="abs person"><div class="name">Daniel Marsh</div><div class="role">CEO at Tessaro</div></div>
<p class="abs quote-text">Sed ut perspiciatis unde omnis iste natus error sit voluptatem accusantium doloremque laudantium, totam rem aperiam, eaque ipsa quae ab illo inventore veritatis et quasi architecto beatae vitae dicta sunt explicabo. Nemo enim ipsam voluptatem quia voluptas sit aspernatur aut odit aut fugit, sed quia consequuntur magni dolores eos qui ratione voluptatem sequi nesciunt.</p>
<div class="abs quote-dots"><span class="on"></span><span></span><span></span><span></span></div>

<section class="section contact">
  <h2 class="abs section-title" style="top:85px">Get in touch</h2>
  <p class="abs section-intro" style="top:168px;left:244px;width:712px">Sed ut perspiciatis unde omnis iste natus error sit voluptatem accusantium doloremque laudantium, totam rem aperiam, eaque ipsa quae ab illo inventore veritatis et quasi architecto beatae vitae dicta sunt explicabo. Nemo enim ipsam voluptatem quia voluptas sit aspernatur aut odit aut fugit.</p>
</section>
<div class="abs phone" role="img" aria-label="Smartphone illustration with a hello speech bubble and the brand on a green screen"></div>
<div class="abs say-hello">Say hello!</div>
<div class="abs field" style="top:2740px">Name</div>
<div class="abs field" style="top:2793px">Email</div>
<div class="abs field" style="top:2849px">Message</div>
<div class="abs send">
  <svg width="28" height="18" viewBox="0 0 28 18" fill="none" stroke="#555" stroke-width="1.4"><rect x="1" y="1" width="26" height="16"/><path d="M1 1l13 9 13-9"/></svg>
  Send message
</div>

<footer class="section footer">
  <div class="abs" style="left:162px;top:102px;width:200px">
    <h4>About Us</h4>
    <p style="margin-top:20px">eiusmod tempor incididunt ut labore et dolore magna aliqua. Ut enim ad minim veniam, quis nostrud exercitation ullamco labore nisi ut aliquip ex ea commodo consequat.</p>
  </div>
  <div class="abs" style="left:387px;top:102px">
    <h4>Subscribe</h4>
    <p style="margin-top:26px">Get updated for our newsletter</p>
  </div>
  <div class="abs links" style="left:687px;top:102px">
    <h4>Useful Links</h4>
    <ul style="margin-top:18px"><li>About Us</li><li>Services</li><li>News</li><li>Contact Us</li></ul>
  </div>
</footer>
<div class="abs subscribe-box">
  <svg width="14" height="10" viewBox="0 0 14 10" fill="none" stroke="#999" stroke-width="1.2"><path d="M0 5h12M8 1l4 4-4 4"/></svg>
</div>
<div class="abs brand footer-brand"><span class="mark"></span>VOLNOR mobile</div>
<p class="abs copyright" style="font-size:9.5px;color:var(--text)">© 2015 Volnor. All Rights Reserved.</p>

</body>
</html>
```